Counsel Atelier

we need all the matirials for the office to speak with the internet site
www.corvenfirm-example.com

look stilish and modern yet very respecteble

our logo needs to be our logo and some times

just the letters " Corven " done nicely.

We need to send e mails with a design

Firm paper

and our gmail products to look nice when we use google docs

so we need a place for

lawers names and

the corven

and logo

and address

and some one to help us do it all

Target Market(s)

Big firms

Industry/Entity Type

Law Firm

Font styles to use
Serif

Requirements
Must have
• Rememrable
• Different yet respectable
• For multi languages
• LAW
• B
• LAWYERS
• BOUTIQUE
Nice to have
• Clean Design
• impressive
• i put on a new card i liked
• We should not put any decorations and beautiful logo
• it's against the law for lawyers
• I have a card that proves that we are smart and boutiques
• This card that I attached as an example
• Makes you little work, and certainly - apart from everyone
• Would love this design idea
• The numbers stated hiding it from top to bottom
• I put my real information integration profile
• The thing is that people should enlighten other options and other card
• This should be accessible designer fee changes
• Still very respectable and serious
• it needs to say among other creative stuff
• Counsel atelier CORVEN
• MARCUS TELLION
• 052-7196205
• 1@corvenfirm-example.com
• www.corvenfirm-example.com
• but any smart idea
Should not have
• We have a problam
• It turns out that the law of the Bar Association in
• Our country
• Do not allow to put the firm logo on business cards
• Or office paper
• the logo can only be letters and names
• So we should convey the idea of all sorts of areas along
• As we tried with our logo
• Through the letters themselves
• And their integration with each other

```html
<!DOCTYPE html>
<html lang="en">
<head>
<meta charset="utf-8">
<title>Corven — Business Card</title>
<link rel="stylesheet" href="https://fonts.googleapis.com/css2?family=Cinzel:wght@400;600&family=Tinos&display=swap">
<style>
  :root {
    --backdrop: #e9e9eb;
    --paper: #f4f4f6;
    --navy: #0d2a62;
    --ink-navy: #14306a;
    --ink-grey: #3c3f47;
    --reverse-ink: #e6e8ef;
  }
  * { margin: 0; padding: 0; box-sizing: border-box; }
  html, body {
    width: 1105px; height: 1200px; overflow: hidden;
    background: var(--backdrop);
  }
  .canvas { position: relative; width: 1105px; height: 1200px; }

  .card {
    position: absolute; left: 182px; width: 746px; height: 427px;
  }
  .card--front { top: 119px; background: var(--paper); }
  .card--back  { top: 637px; background: var(--navy); }

  /* Front */
  .firm-block {
    position: absolute; left: 46px; top: 150px;
  }
  .firm-name {
    font-family: "Cinzel", serif; font-weight: 600;
    font-size: 52px; letter-spacing: .02em;
    color: var(--ink-navy); line-height: 1;
  }
  .firm-tagline {
    margin-top: 6px; padding-left: 3px;
    font-family: "Cinzel", serif; font-weight: 400;
    font-size: 14px; letter-spacing: .32em;
    color: var(--ink-grey); line-height: 1;
  }
  .address {
    position: absolute; left: 49px; top: 236px;
    font-family: "Tinos", serif; font-size: 20px;
    line-height: 27px; color: var(--ink-grey);
  }
  .contacts {
    position: absolute; left: 49px; top: 296px;
    list-style: none;
    font-family: "Tinos", serif; font-size: 20px; color: var(--ink-grey);
  }
  .contacts li { display: flex; align-items: center; height: 29px; }
  .contacts svg { width: 17px; height: 17px; margin-right: 12px; fill: var(--ink-navy); }

  .person {
    position: absolute; right: 47px; top: 262px; text-align: right;
    font-family: "Cinzel", serif; color: var(--ink-navy);
  }
  .person-name { font-size: 30px; letter-spacing: .03em; line-height: 1.1; }
  .person-role { font-size: 19px; letter-spacing: .08em; color: var(--ink-grey); margin-top: 6px; }
  .accent-bar {
    position: absolute; right: 0; top: 268px; width: 17px; height: 56px;
    background: var(--navy);
  }

  /* Back */
  .back-lockup {
    position: absolute; left: 0; right: 0; top: 170px; text-align: center;
  }
  .back-name {
    font-family: "Cinzel", serif; font-weight: 600;
    font-size: 62px; letter-spacing: .02em; line-height: 1;
    color: var(--reverse-ink);
  }
  .back-tagline {
    margin-top: 12px;
    font-family: "Cinzel", serif; font-weight: 400;
    font-size: 16px; letter-spacing: .36em; line-height: 1;
    color: var(--reverse-ink);
  }
  .back-url {
    position: absolute; left: 0; right: 0; top: 355px; text-align: center;
    font-family: "Tinos", serif; font-size: 20px;
    letter-spacing: .45em; color: var(--reverse-ink);
  }
</style>
</head>
<body>
<main class="canvas">

  <section class="card card--front" aria-label="Business card front">
    <div class="firm-block">
      <h1 class="firm-name">CORVEN</h1>
      <p class="firm-tagline">COUNSEL ATELIER</p>
    </div>
    <p class="address">4120 Harbor Ridge Road<br>Juneau, Alaska 99801</p>
    <ul class="contacts">
      <li>
        <svg viewBox="0 0 24 24" aria-hidden="true"><path d="M6.6 10.8a15.1 15.1 0 0 0 6.6 6.6l2.2-2.2a1 1 0 0 1 1-.25 11.4 11.4 0 0 0 3.6.57 1 1 0 0 1 1 1V20a1 1 0 0 1-1 1A17 17 0 0 1 3 4a1 1 0 0 1 1-1h3.5a1 1 0 0 1 1 1c0 1.250.2 2.45.57 3.6a1 1 0 0 1-.25 1z"/></svg>
        052 719 6205
      </li>
      <li>
        <svg viewBox="0 0 24 24" aria-hidden="true"><path d="M2 5h20v14H2z M3.5 6.5 12 13l8.5-6.5" fill="none" stroke="#14306a" stroke-width="2"/><path d="M2 5h20L12 12.5z"/></svg>
        mtellion@corvenfirm-example.com
      </li>
      <li>
        <svg viewBox="0 0 24 24" aria-hidden="true"><circle cx="12" cy="12" r="10"/><path d="M2 12h20M12 2c3 3 3 17 0 20M12 2c-3 3-3 17 0 20" fill="none" stroke="#f4f4f6" stroke-width="1.4"/></svg>
        www.corvenfirm-example.com
      </li>
    </ul>
    <div class="person">
      <p class="person-name">Marcus Tellion</p>
      <p class="person-role">Attorney</p>
    </div>
    <div class="accent-bar"></div>
  </section>

  <section class="card card--back" aria-label="Business card back">
    <div class="back-lockup">
      <p class="back-name">CORVEN</p>
      <p class="back-tagline">COUNSEL ATELIER</p>
    </div>
    <p class="back-url">www.corvenfirm-example.com</p>
  </section>

</main>
</body>
</html>
```